Granite Haulers Guild

This piece is to drive tow companies and drivers to join the largest towing association within the state of Texas. It will be 3 pieces. A cover sheet that is mostly graphic with minimal copy, page two will be a letter and is not required for this exercise, page three will be a list of membership benefits and the pricing for each level. I have attached copy and their current logo. However, I DO NOT WANT the logo to drive the design. We need outside of the box thinking that is not confined to the limitations the logo presents.

Target Market(s)

Tow truck companies and drivers. Male 20 to 60 years old.

Industry/Entity Type

Pricing

Requirements
Must have
• The cover sheet must say "Let's Pick Each Other Up" the rest is all graphic and up to your discretion.

Would prefer a Southwestern/Texas type of feel. Down home. Family oriented. We're in this together type of flavor.

Must boldly promote price levels and options for signing up on page three.

Must use the attached copy for page three.
Should not have
• Clipart, Illustrations, ugliness

```html
<!DOCTYPE html>
<html lang="en">
<head>
<meta charset="utf-8">
<title>Granite Haulers Guild – Information Package</title>
<link rel="stylesheet" href="https://fonts.googleapis.com/css2?family=Oswald:wght@500;700&family=Crimson+Text:wght@400;600&family=Arimo:wght@400;700&display=swap">
<style>
  :root {
    --rust: #a85a1e;
    --oxblood: #800000;
    --gold: #dcb20c;
    --ink: #1f1d3a;
    --bar-red: #7e0c0c;
    --paper-bg: #ffffff;
    --white: #ffffff;
  }
  * { box-sizing: border-box; margin: 0; padding: 0; }
  html, body { width: 1200px; height: 1000px; overflow: hidden; background: var(--paper-bg); }
  .canvas { position: relative; width: 1200px; height: 1000px; }

  .sheet {
    position: absolute;
    width: 460px;
    height: 585px;
    box-shadow: 4px 5px 8px rgba(0,0,0,0.35);
    overflow: hidden;
  }

  /* Benefits page (lies on top of the cover) */
  .benefits-page { left: 28px; top: 8px; background: var(--gold); z-index: 2; }
  .benefits-page .sidebar {
    position: absolute; left: 0; top: 0; bottom: 0; width: 160px;
    background: var(--rust); color: var(--white);
    padding: 18px 18px 0 14px;
    border-right: 2px dashed var(--oxblood);
  }
  .sidebar-headline {
    font-family: "Oswald", sans-serif; font-weight: 700; font-size: 13px; letter-spacing: 0.3px;
    text-align: center; margin-bottom: 20px;
  }
  .sidebar p {
    font-family: "Crimson Text", serif; font-size: 12px; line-height: 1.22;
    text-align: justify; margin-bottom: 14px;
  }
  .benefits-body { position: absolute; left: 160px; top: 0; right: 0; bottom: 0; color: var(--ink); }
  .tier-bar {
    position: absolute; right: 0; height: 26px;
    background: var(--bar-red); color: var(--white);
    font-family: "Oswald", sans-serif; font-weight: 700; font-size: 12.5px; letter-spacing: 0.3px;
    display: flex; align-items: center; justify-content: center;
  }
  .tier-bar.premier { top: 6px; left: 18px; }
  .tier-bar.executive { top: 320px; left: 28px; }
  .tier-bar.basic { top: 474px; left: 32px; }
  .tier-block { position: absolute; left: 0; right: 12px; font-family: "Arimo", sans-serif; font-size: 8.4px; line-height: 1.5; }
  .tier-block.premier { top: 40px; padding-left: 6px; }
  .tier-block.executive { top: 354px; padding-left: 10px; }
  .tier-block.basic { top: 508px; padding-left: 10px; }
  .tier-intro { margin-bottom: 10px; }
  .benefit { margin-bottom: 12px; }
  .benefit > p:not(.benefit-title) { padding-left: 4px; }
  .benefit-title { color: var(--oxblood); padding-left: 6px; }
  .benefit-title::before { content: "•"; margin-right: 12px; color: var(--oxblood); }

  /* Cover page */
  .cover-page { left: 390px; top: 382px; height: 590px; background: var(--oxblood); z-index: 1; }
  .cover-page .spine {
    position: absolute; left: 0; top: 0; bottom: 0; width: 148px;
    background: var(--rust);
    border-right: 2px dashed var(--gold);
  }
  .cover-title {
    position: absolute; left: 150px; right: 0; top: 74px; text-align: center;
    font-family: "Oswald", sans-serif; font-weight: 700; font-size: 21px; letter-spacing: 2px; color: var(--gold);
  }
  .cover-subtitle {
    position: absolute; left: 150px; right: 0; top: 132px; text-align: center;
    font-family: "Oswald", sans-serif; font-weight: 700; font-size: 11px; letter-spacing: 0.5px; color: var(--white);
  }
  .cover-mark {
    position: absolute; left: 222px; top: 240px; width: 180px;
    display: flex; align-items: center; gap: 8px;
    font-family: "Oswald", sans-serif; font-weight: 700; font-size: 20px; line-height: 1.1; color: var(--white);
  }
  .cover-mark .dot { width: 16px; height: 16px; background: var(--white); border-radius: 50%; flex: none; }
</style>
</head>
<body>
<main class="canvas">

  <section class="sheet cover-page" aria-label="Cover">
    <div class="spine"></div>
    <h1 class="cover-title">Let’s Pick Each Other Up</h1>
    <p class="cover-subtitle">An Information Package for Prospective Members</p>
    <div class="cover-mark">
      <span class="dot"></span>
      <span>Granite Haulers Guild</span>
    </div>
  </section>

  <section class="sheet benefits-page" aria-label="Membership benefits">
    <aside class="sidebar">
      <h2 class="sidebar-headline">Headline</h2>
      <p>This area could contain background history and statistical information on the association in order to help build credibility.</p>
      <p>Could it even include a list of other tow operations that your new prospects might recognize?</p>
      <p>Information is usually more readable if it is displayed in little chunks so sidebars like this are a perfect vehicle for that.</p>
    </aside>

    <div class="benefits-body">
      <h3 class="tier-bar premier">$1,000 Premier Membership</h3>
      <div class="tier-block premier">
        <p class="tier-intro">Includes all the benefits you get today plus:</p>
        <div class="benefit">
          <p class="benefit-title">Free Legal Consulting</p>
          <p>With this membership you can call a lawyer up every time TRLB hits you with a fine or a threat and ask for advice. If you need representation you get it at a discount.</p>
        </div>
        <div class="benefit">
          <p class="benefit-title">Free IM Training</p>
          <p>As an owner your IM training is free.</p>
        </div>
        <div class="benefit">
          <p class="benefit-title">Staffing Requirements</p>
          <p>You tell us how many drivers you need and we will help you find them. We have a list with over 300 people waiting for work.</p>
        </div>
        <div class="benefit">
          <p class="benefit-title">“Annual Towers Get Away”</p>
          <p>Once a year we will find a resort that you and your spouse can go to with other leaders in the industry. We’ll meet for an hour and play for the weekend. Have fun and get a tax write off.</p>
        </div>
        <div class="benefit">
          <p class="benefit-title">Quarterly Strategy Meetings</p>
          <p>We lock ourselves up in a room for a day and plan the future of the industry. Work on problems, write laws and identify company needs.</p>
        </div>
      </div>

      <h3 class="tier-bar executive">$500 Executive Membership</h3>
      <div class="tier-block executive">
        <p class="tier-intro">Includes all you get today plus:</p>
        <div class="benefit">
          <p class="benefit-title">Free Legal Consulting</p>
          <p>With this membership you can call a lawyer up every time TRLB hits you with a fine or a threat and ask for advice. If you need representation you get it at a discount</p>
        </div>
        <div class="benefit">
          <p class="benefit-title">IM Training for only $75</p>
          <p>That’s a 50% savings for your IM training (Owner)</p>
        </div>
      </div>

      <h3 class="tier-bar basic">$200 Basic Membership</h3>
      <div class="tier-block basic">
        <p>All the great benefits you get today</p>
      </div>
    </div>
  </section>

</main>
</body>
</html>
```